Brochure Design for a Corporate Anti-Counterfeiting and Brand Protection Agency

We need a very professional brochure designed for our company Norvane Partners and in particular our brand protection services. We are a global brand investigation and brand protection agency that helps organisations to combat cyber crime and counterfeiting.

The brochure will need be extremely professional and will be used at conferences when competing with many other providers.

We have a comprehensive brand book that must be carefully read and understood to align the design with our existing brand.

We would like the new brochure design to be very similar to our old brochure which is named "Norvane Partners Brochure v34" except be completely aligned with our new brand identity which is in the brandbook and evident on our website; www.norvanepartners.example. The content can be the same but would prefer some new visual diagrams explaining points and more icons etc.

I have also attached a few of old and new brand protection presentations, brochures, proposals where you can find the relevant ideas, concepts and where you will find all the content to be used in the brochure.

I am looking for the design direction more than the correct content, I will request the adobe files and make the relevant changes to content myself. More interested in seeing the design of the brochure.

Thank you, I look forward to seeing your design.

Meric.

Industry/Entity Type

It Company

```html
<!DOCTYPE html>
<html lang="en">
<head>
<meta charset="utf-8">
<title>Norvane Partners Brochure</title>
<link rel="stylesheet" href="https://fonts.googleapis.com/css2?family=Crimson+Pro:wght@400;500&family=Raleway:wght@300;400;600&display=swap">
<style>
:root{
  --ink:#1e1f22;
  --charcoal:#2c2d31;
  --slate:#3a3b3f;
  --steel:#55565b;
  --mist:#8c8d91;
  --gold:#c8962a;
  --paper:#ffffff;
  --text:#3b3b3b;
  --soft:#9a9a9a;
}
*{margin:0;padding:0;box-sizing:border-box}
html,body{width:1200px;height:909px;overflow:hidden;background:var(--paper)}
body{position:relative;font-family:"Raleway",sans-serif;color:var(--text)}
.abs{position:absolute}
.page{position:absolute;overflow:hidden;background:var(--paper);box-shadow:0 1px 3px rgba(0,0,0,.18)}
.serif{font-family:"Crimson Pro",serif}
.logo{position:absolute;font-family:"Crimson Pro",serif;font-weight:400;color:#fff;line-height:1;text-align:center}
.logo .name{display:block;font-size:21px;letter-spacing:1px}
.logo .sub{display:block;font-size:3.6px;letter-spacing:2.4px;margin-top:2px}
.photo{position:absolute}
.gold-rule{position:absolute;height:3px;background:var(--gold)}
.heading{position:absolute;font-family:"Crimson Pro",serif;font-weight:400;color:var(--ink);font-size:13.5px;line-height:12.5px}
.body-copy{position:absolute;font-size:3.6px;line-height:4.6px;color:var(--text)}
.body-copy p{margin-bottom:3.4px}
.lead{position:absolute;font-weight:300;font-size:6.6px;line-height:7.4px;color:var(--mist)}
.folio{position:absolute;font-size:3px;color:var(--steel);letter-spacing:.2px}
.section-title{position:absolute;font-weight:300;font-size:6.4px;color:var(--soft)}
.title-rule{position:absolute;height:1px;background:var(--gold);opacity:.7}
.icon{position:absolute}
.icon svg{display:block;stroke:var(--gold);fill:none;stroke-width:1.4}
.url{position:absolute;font-weight:600;font-size:5.6px;letter-spacing:1px;color:var(--ink);white-space:nowrap}
.contents-list{position:absolute;list-style:none;font-size:3.7px;color:#6a6f8a}
.contents-list li{display:flex;justify-content:space-between;height:6.9px;border-bottom:.5px solid var(--gold);align-items:flex-end;padding-bottom:.4px}
.contents-list li.active{background:rgba(200,150,42,.55);color:#fff}
.benefit-title{position:absolute;font-weight:300;font-size:6.6px;color:var(--soft);white-space:nowrap}
.benefit-copy{position:absolute;font-size:3.6px;line-height:4.4px;color:var(--text);width:98px}
</style>
</head>
<body>

<section class="page cover-front" style="left:139px;top:66px;width:259px;height:366px;background:var(--charcoal)">
  <div class="abs" style="left:0;top:0;width:259px;height:62px;background:var(--ink)"></div>
  <div class="logo" style="left:22px;top:15px"><span class="name">NORVANE</span><span class="sub">PARTNERS</span></div>
  <div class="abs" style="left:0;top:62px;width:259px;height:8px;background:var(--steel)"></div>
  <div class="abs" style="left:0;top:60px;width:112px;height:6px;background:var(--mist)"></div>
  <div class="photo" role="img" aria-label="Close-up of hands typing on a laptop keyboard in low light" style="left:0;top:70px;width:259px;height:216px;background:radial-gradient(ellipse at 70% 55%,#8a8b8e 0%,#4a4b4f 45%,#1c1d20 100%)"></div>
  <h1 class="serif abs" style="left:17px;top:79px;color:#fff;font-weight:400;font-size:23px;line-height:23.5px;letter-spacing:.3px">TRUSTED<br>FOR WHAT<br>IS BROUGHT<br>TO LIGHT</h1>
  <div class="gold-rule" style="left:0;top:176px;width:124px"></div>
  <div class="abs" style="left:0;top:286px;width:259px;height:52px;background:#242528"></div>
  <div class="abs" style="left:0;top:280px;width:259px;height:8px;background:var(--slate)"></div>
  <p class="serif abs" style="right:16px;top:296px;text-align:right;color:var(--gold);font-size:8.2px;line-height:10px">Combating and safeguarding against cybercrime.<br>Around the world, around the clock.</p>
  <div class="abs" style="left:0;top:338px;width:259px;height:28px;background:var(--paper)"></div>
  <div class="abs" style="left:0;top:349px;width:96px;height:17px;background:var(--charcoal)"></div>
  <div class="url" style="right:14px;top:350px">NORVANEPARTNERS.EXAMPLE</div>
  <div class="abs" style="left:0;top:362px;width:259px;height:4px;background:var(--charcoal)"></div>
</section>

<section class="page spread-intro" style="left:528px;top:66px;width:517px;height:366px">
  <div class="abs" style="left:0;top:0;width:125px;height:114px;background:var(--ink)"></div>
  <div class="photo" role="img" aria-label="Dark monochrome office interior" style="left:125px;top:0;width:134px;height:108px;background:linear-gradient(90deg,#3c3d41,#5a5b5f)"></div>
  <div class="photo" role="img" aria-label="Silhouette of a rooftop building with satellite dish against a grey sky" style="left:259px;top:0;width:258px;height:108px;background:linear-gradient(180deg,#6a6b6f 0%,#4a4b4f 50%,#1d1e21 100%)"></div>
  <div class="logo" style="left:16px;top:16px"><span class="name">NORVANE</span><span class="sub">PARTNERS</span></div>
  <div class="logo" style="right:16px;top:16px"><span class="name">NORVANE</span><span class="sub">PARTNERS</span></div>
  <p class="serif abs" style="left:140px;top:55px;width:102px;text-align:right;color:var(--gold);font-size:13px;line-height:14px">Navigating<br>the inaccessible</p>
  <div class="gold-rule" style="left:374px;top:76px;width:56px"></div>
  <div class="abs" style="left:0;top:108px;width:517px;height:6px;background:var(--mist)"></div>

  <h2 class="heading" style="left:16px;top:138px">International cyber<br>investigation agency</h2>
  <div class="gold-rule" style="left:16px;top:172px;width:106px"></div>
  <div class="body-copy" style="left:16px;top:190px;width:106px">
    <p>Our head office operates a fully staffed monitoring centre that watches online marketplaces, social platforms and trade channels around the clock. We act quickly to protect corporations and individuals from a wide range of threats across every continent and in every jurisdiction.</p>
    <p>Norvane Partners goes beyond traditional methods by joining cyber intelligence, investigations and on the ground enforcement into a single service. This lets us identify key offenders, uncover actionable intelligence and collect legal evidence for court proceedings.</p>
    <p>We deliver services that are not available elsewhere in the market. Our focused culture ensures every case is handled with a high degree of urgency and sensitivity.</p>
  </div>
  <div class="gold-rule" style="left:138px;top:236px;width:106px;height:2px"></div>
  <div class="photo" role="img" aria-label="Portrait of the chief executive" style="left:138px;top:243px;width:49px;height:62px;background:linear-gradient(180deg,#8d8e92,#2b2c2f)"></div>
  <div class="abs" style="left:138px;top:308px;font-weight:300;font-size:6px;color:var(--mist)">Alden Marsh</div>
  <div class="abs" style="left:138px;top:316px;font-weight:600;font-size:3.2px;color:var(--ink)">CEO &amp; Executive Chairman</div>
  <div class="body-copy" style="left:194px;top:243px;width:50px;font-size:3px;line-height:3.9px;color:var(--mist)">Alden Marsh is an accomplished cybercrime expert and investigator with over twenty years of experience working with governments, corporations and individuals on complex matters of fraud, piracy and reputation.</div>

  <div class="photo" role="img" aria-label="Soft-focus black and white desk scene with a glass" style="left:259px;top:134px;width:258px;height:203px;background:radial-gradient(ellipse at 25% 65%,#bdbdbd 0%,#dedede 40%,#e9e9e9 75%,#8e8e8e 100%)"></div>
  <h2 class="heading" style="left:394px;top:150px;font-size:12px">Contents</h2>
  <div class="gold-rule" style="left:394px;top:172px;width:86px"></div>
  <ul class="contents-list" style="left:394px;top:186px;width:88px">
    <li><span>Intelligence &amp; Enforcement Solutions</span><span>4</span></li>
    <li><span>Integrated Solutions &amp; Services</span><span>5</span></li>
    <li><span>Norvane Brand Protection Results</span><span>6</span></li>
    <li><span>Our Values</span><span>6</span></li>
    <li><span>Some Hard Facts</span><span>6</span></li>
    <li><span>Investigators, Experts &amp; Analysts</span><span>7</span></li>
    <li><span>Integrated Solutions, One Objective</span><span>7</span></li>
    <li><span>Some Recent Projects</span><span>8</span></li>
    <li><span>Intelligence &amp; Enforcement Solutions</span><span>8</span></li>
    <li class="active"><span>Integrated Solutions &amp; Services</span><span>9</span></li>
    <li><span>Norvane Brand Protection Results</span><span>10</span></li>
    <li><span>Integrated Solutions &amp; Services</span><span>11</span></li>
    <li><span>Some Hard Facts</span><span>12</span></li>
    <li><span>Investigators, Experts &amp; Analysts</span><span>13</span></li>
  </ul>

  <div class="folio" style="left:16px;top:349px">2</div>
  <div class="folio" style="left:33px;top:349px">NORVANE PARTNERS International Cyber Investigation Agency 2017</div>
  <div class="folio" style="left:376px;top:349px">NORVANE PARTNERS International Cyber Investigation Agency 2017</div>
  <div class="folio" style="left:498px;top:349px">3</div>
  <div class="abs" style="left:162px;top:350px;width:97px;height:16px;background:var(--charcoal)"></div>
  <div class="abs" style="left:259px;top:357px;width:258px;height:9px;background:var(--charcoal)"></div>
</section>

<section class="page spread-solutions" style="left:181px;top:481px;width:520px;height:368px">
  <div class="logo" style="left:16px;top:15px;color:var(--ink)"><span class="name">NORVANE</span><span class="sub">PARTNERS</span></div>
  <div class="abs" style="left:0;top:65px;width:66px;height:9px;background:var(--charcoal)"></div>
  <div class="abs" style="left:38px;top:70px;width:28px;height:5px;background:var(--mist)"></div>

  <h2 class="heading" style="left:16px;top:103px">Intelligence &amp;<br>Enforcement<br>Solutions</h2>
  <div class="gold-rule" style="left:16px;top:148px;width:82px"></div>
  <p class="lead" style="left:16px;top:159px;width:84px">The results matter most. It's our passion. Dedication and attention to details are what set us apart.</p>

  <div class="section-title" style="left:119px;top:35px">Global Investigations</div>
  <div class="title-rule" style="left:119px;top:46px;width:124px"></div>
  <div class="icon" style="left:119px;top:56px"><svg width="28" height="28" viewBox="0 0 28 28"><circle cx="15" cy="13" r="10"/><path d="M5 13h20M15 3c-5 6-5 14 0 20M15 3c5 6 5 14 0 20"/><path d="M4 24l5-5"/></svg></div>
  <div class="section-title" style="left:119px;top:104px">Brand Protection</div>
  <div class="title-rule" style="left:119px;top:115px;width:124px"></div>
  <div class="icon" style="left:119px;top:124px"><svg width="28" height="28" viewBox="0 0 28 28"><path d="M14 3l9 4v7c0 6-4 9-9 11-5-2-9-5-9-11V7z"/><circle cx="17" cy="15" r="6"/></svg></div>
  <div class="section-title" style="left:119px;top:173px">Cyber Intelligence</div>
  <div class="title-rule" style="left:119px;top:184px;width:124px"></div>
  <div class="icon" style="left:119px;top:192px"><svg width="28" height="28" viewBox="0 0 28 28"><circle cx="6" cy="8" r="2"/><circle cx="20" cy="6" r="2"/><circle cx="14" cy="14" r="2"/><circle cx="5" cy="21" r="2"/><circle cx="22" cy="20" r="2"/><path d="M6 8l8 6 6-8M14 14l-9 7M14 14l8 6"/></svg></div>

  <div class="body-copy" style="left:151px;top:52px;width:92px"><p>Our investigation operations uncover fraud, piracy, counterfeiting and other crimes that damage your reputation, brand equity and customer loyalty. Counterfeit trade costs global brands billions each year, and only a small share is ever stopped on the ground.</p></div>
  <div class="body-copy" style="left:151px;top:121px;width:92px"><p>Our investigation operations uncover fraud, piracy, counterfeiting and other crimes that damage your reputation, brand equity and customer loyalty. Counterfeit trade costs global brands billions each year, and only a small share is ever stopped on the ground.</p></div>
  <div class="body-copy" style="left:151px;top:189px;width:92px"><p>Our investigation operations uncover fraud, piracy, counterfeiting and other crimes that damage your reputation, brand equity and customer loyalty. Counterfeit trade costs global brands billions each year, and only a small share is ever stopped on the ground.</p></div>

  <div class="abs" style="left:16px;top:247px;width:100px;height:7px;background:var(--steel)"></div>
  <div class="photo" role="img" aria-label="Fingerprint merging with binary code on a dark background" style="left:0;top:254px;width:260px;height:85px;background:linear-gradient(90deg,#8a8b8e 0%,#3a3b3e 45%,#1e1f22 100%)"></div>
  <p class="serif abs" style="right:277px;top:280px;text-align:right;color:var(--gold);font-size:12px;line-height:13px;white-space:nowrap">What's your's is your's.<br>We want to help you<br>keep it that way.</p>

  <div class="photo" role="img" aria-label="Close-up of a printed confidentiality agreement" style="left:260px;top:0;width:260px;height:90px;background:linear-gradient(180deg,#bfbfbf 0%,#8e8e8e 55%,#5c5c5c 100%)"></div>
  <div class="logo" style="right:17px;top:15px;color:var(--ink)"><span class="name">NORVANE</span><span class="sub">PARTNERS</span></div>
  <div class="gold-rule" style="left:466px;top:61px;width:54px"></div>
  <div class="abs" style="left:407px;top:90px;width:98px;height:6px;background:var(--charcoal)"></div>

  <h2 class="heading" style="left:275px;top:103px">Integrated<br>Solutions<br>&amp; Services</h2>
  <div class="gold-rule" style="left:275px;top:148px;width:82px"></div>
  <p class="lead" style="left:275px;top:159px;width:68px">Brands face new risks and threats every day, global brands need an</p>
  <div class="body-copy" style="left:275px;top:195px;width:80px">
    <p>The Norvane Brand Protection solution is the only proactive solution that goes beyond traditional methods and instead integrates cyber intelligence, investigations, monitoring and enforcement into an end to end brand protection service built on twenty years of investigative experience.</p>
    <p>This enables us to identify operators on the ground and take action to eliminate offenders and disrupt your cyber crime threats. The Norvane Sentinel system protects your revenues through identification and disruption of promotion and distribution channels online.</p>
    <p>The Norvane Brand Protection Program can reduce the number of infringements by up to 95% in the first eight months. The solution goes a step further by identifying and shutting down operations on the ground.</p>
  </div>

  <div class="icon" style="left:381px;top:119px"><svg width="20" height="20" viewBox="0 0 20 20"><circle cx="10" cy="10" r="8"/><path d="M12.5 6.5h-3.5a2 2 0 000 4h2a2 2 0 010 4h-3.5M10 4.5v11"/></svg></div>
  <div class="benefit-title" style="left:406px;top:115px">Improved Roi</div>
  <div class="title-rule" style="left:406px;top:124px;width:98px"></div>
  <div class="benefit-copy" style="left:406px;top:127px">Companies often see a 60:1 ROI in terms of money saved vs money spent. As well as more benefits that reach well into the future.</div>

  <div class="icon" style="left:381px;top:153px"><svg width="20" height="20" viewBox="0 0 20 20"><path d="M1 8l4-3 4 2 3-2 4 1 3 3M3 9l5 5 2-1 2 1 4-4M8 10l2 2"/></svg></div>
  <div class="benefit-title" style="left:406px;top:149px">Increased Brand Loyalty</div>
  <div class="title-rule" style="left:406px;top:158px;width:98px"></div>
  <div class="benefit-copy" style="left:406px;top:161px">Companies often see a 60:1 ROI in terms of money saved vs money spent. As well as more benefits that reach well into the future.</div>

  <div class="icon" style="left:381px;top:187px"><svg width="20" height="20" viewBox="0 0 20 20"><path d="M10 2l2.4 5 5.5.6-4 3.8 1.1 5.4L10 14l-5 2.8 1.1-5.4-4-3.8 5.5-.6z"/></svg></div>
  <div class="benefit-title" style="left:406px;top:183px">Higher Customer Satisfaction</div>
  <div class="title-rule" style="left:406px;top:192px;width:98px"></div>
  <div class="benefit-copy" style="left:406px;top:195px">Companies often see a 60:1 ROI in terms of money saved vs money spent. As well as more benefits that reach well into the future.</div>

  <div class="icon" style="left:381px;top:221px"><svg width="20" height="20" viewBox="0 0 20 20"><path d="M10 1.5l7 3v5c0 5-3 7.5-7 9-4-1.5-7-4-7-9v-5z"/><path d="M6.5 10l2.5 2.5 4.5-5"/></svg></div>
  <div class="benefit-title" style="left:406px;top:217px">Improved Safety</div>
  <div class="title-rule" style="left:406px;top:226px;width:98px"></div>
  <div class="benefit-copy" style="left:406px;top:229px">Companies often see a 60:1 ROI in terms of money saved vs money spent. As well as more benefits that reach well into the future.</div>

  <div class="icon" style="left:381px;top:258px"><svg width="20" height="20" viewBox="0 0 20 20"><circle cx="9" cy="10" r="7"/><path d="M7 14V6h3a2 2 0 010 4H7M10 10l3 4M13 15l5 2"/></svg></div>
  <div class="benefit-title" style="left:406px;top:255px">Healthier Brand Image</div>
  <div class="title-rule" style="left:406px;top:264px;width:98px"></div>
  <div class="benefit-copy" style="left:406px;top:267px">Companies often see a 60:1 ROI in terms of money saved vs money spent. As well as more benefits that reach well into the future.</div>

  <div class="icon" style="left:381px;top:297px"><svg width="20" height="20" viewBox="0 0 20 20"><path d="M2 18h16M4 18v-5h3v5M8.5 18v-8h3v8M13 18v-11h3v11M3 10l5-4 3 2 6-5"/></svg></div>
  <div class="benefit-title" style="left:406px;top:291px;line-height:8px">Optimised<br>Marketing Investments</div>
  <div class="title-rule" style="left:406px;top:308px;width:98px"></div>
  <div class="benefit-copy" style="left:406px;top:311px">Companies often see a 60:1 ROI in terms of money saved vs money spent. As well as more benefits that reach well into the future.</div>

  <div class="folio" style="left:16px;top:344px">4</div>
  <div class="folio" style="left:33px;top:344px">NORVANE PARTNERS International Cyber Investigation Agency 2017</div>
  <div class="folio" style="left:377px;top:344px">NORVANE PARTNERS International Cyber Investigation Agency 2017</div>
  <div class="folio" style="left:500px;top:344px">5</div>
  <div class="abs" style="left:163px;top:351px;width:357px;height:17px;background:var(--charcoal)"></div>
</section>

<section class="page cover-back" style="left:824px;top:482px;width:260px;height:367px;background:var(--slate)">
  <div class="abs" style="left:0;top:58px;width:116px;height:12px;background:var(--ink)"></div>
  <div class="abs" style="left:128px;top:68px;width:132px;height:6px;background:var(--mist)"></div>
  <div class="photo" role="img" aria-label="Angled close-up of code on a monitor" style="left:116px;top:74px;width:144px;height:204px;background:linear-gradient(135deg,#1c1d20 0%,#6e6f73 45%,#2a2b2e 75%,#111214 100%)"></div>
  <div class="logo" style="left:67px;top:150px"><span class="name" style="font-size:17px">NORVANE</span><span class="sub" style="font-size:3px">PARTNERS</span></div>
  <div class="abs" style="left:34px;top:182px;width:226px;height:1px;background:var(--gold)"></div>
  <p class="serif abs" style="right:160px;top:189px;text-align:right;color:var(--gold);font-size:4.8px;line-height:6.3px;white-space:nowrap">Norvane Partners Pty Ltd<br>Level 14, 88 Harbour Lane,<br>Eastport 4100<br>+00 2 5550 1234<br>+ 00 2 5550 1288</p>
  <div class="abs" style="left:0;top:278px;width:260px;height:60px;background:var(--charcoal)"></div>
  <div class="abs" style="left:0;top:338px;width:260px;height:29px;background:var(--paper)"></div>
  <div class="url" style="left:30px;top:349px">NORVANEPARTNERS.EXAMPLE</div>
  <div class="abs" style="left:164px;top:350px;width:96px;height:17px;background:var(--charcoal)"></div>
  <div class="abs" style="left:0;top:363px;width:260px;height:4px;background:var(--charcoal)"></div>
</section>

</body>
</html>
```